Business Card and Word .doc header and footer required

I need a business card designed for my cybersecurity consulting company. Also required, is a header and footer to be ued for my word documents.
Attached is the Logo design, font and rgb used.

Industry/Entity Type

Cyber Security Consulting

Contact Information for Business Card

Name, Phone, email, website

Colors
0054AA
0677BA
7BADD7
CADEEF
E8F1F8

Requirements
Must have
• Sleek, modern

```html
<!DOCTYPE html>
<html lang="en">
<head>
<meta charset="utf-8">
<title>Harlow Reach Consulting – Stationery</title>
<link rel="stylesheet" href="https://fonts.googleapis.com/css2?family=Montserrat:wght@700&family=Ubuntu:wght@300;400;700&family=Source+Sans+3:wght@400;700&display=swap">
<style>
  :root {
    --ice: #E8F1F8;
    --sky: #7BADD7;
    --mist: #CADEEF;
    --blue: #0677BA;
    --deep: #0054AA;
    --ink: #0B1C2C;
    --sheet: #FAFAFA;
    --white: #FFFFFF;
  }
  html, body {
    margin: 0;
    width: 1200px;
    height: 1200px;
    overflow: hidden;
    background: var(--white);
  }
  .stage { position: relative; width: 1200px; height: 1200px; }

  .card {
    position: absolute;
    width: 463px;
    height: 299px;
    box-shadow: 6px 6px 8px rgba(0,0,0,0.12);
    overflow: hidden;
  }
  .card--back { left: 94px; top: 61px; background: var(--ice); }
  .card--front { left: 634px; top: 62px; background: var(--ice); }

  .pattern-field {
    position: absolute;
    left: 56px; top: 26px;
    width: 350px; height: 204px;
    border-radius: 12px;
    background: linear-gradient(135deg, var(--mist), #B5D0EA 50%, var(--mist));
  }

  .wordmark {
    font-family: "Montserrat", sans-serif;
    font-weight: 700;
    color: var(--ink);
    text-align: center;
    letter-spacing: 0.5px;
    margin: 0;
  }
  .wordmark__sub { display: block; letter-spacing: 3px; }

  .card--back .wordmark {
    position: absolute; left: 0; right: 0; top: 236px;
    font-size: 21px; line-height: 24px;
  }
  .card--back .wordmark__sub { font-size: 10px; line-height: 14px; }

  .brand-dot {
    position: absolute;
    border-radius: 50%;
    background: var(--blue);
  }

  .card__top { position: absolute; left: 0; top: 0; width: 100%; height: 135px; }
  .card__top .brand-dot { left: 202px; top: 16px; width: 60px; height: 60px; }
  .card__top .wordmark {
    position: absolute; left: 0; right: 0; top: 86px;
    font-size: 20px; line-height: 22px;
  }
  .card__top .wordmark__sub { font-size: 9px; line-height: 13px; }

  .card__band {
    position: absolute; left: 0; top: 135px;
    width: 100%; height: 164px;
    background: var(--sky);
  }
  .person { position: absolute; left: 36px; top: 10px; margin: 0; }
  .person__name {
    font-family: "Ubuntu", sans-serif; font-weight: 300;
    font-size: 24px; line-height: 28px; color: var(--white); margin: 0;
  }
  .person__name strong { font-weight: 700; }
  .person__role {
    font-family: "Ubuntu", sans-serif; font-weight: 400;
    font-size: 17px; line-height: 18px; color: var(--white); margin: 0;
  }

  .contact-list {
    list-style: none; margin: 0; padding: 0;
    position: absolute;
    font-family: "Source Sans 3", sans-serif;
    color: var(--ink);
  }
  .contact-list li { display: flex; align-items: center; }
  .contact-list svg { flex: none; fill: var(--ink); }

  .card__band .contact-list { left: 33px; top: 76px; font-size: 17px; }
  .card__band .contact-list li { height: 25.5px; }
  .card__band .contact-list svg { width: 18px; height: 18px; margin-right: 10px; }

  .letterhead {
    position: absolute; left: 99px; top: 431px;
    width: 998px; height: 780px;
    background: var(--sheet);
    box-shadow: 6px 6px 8px rgba(0,0,0,0.15);
    border-top: 1px solid #E0E4E8;
    border-left: 1px solid #E0E4E8;
  }
  .letterhead__header {
    position: absolute; left: 0; top: 0; width: 100%; height: 156px;
    background: var(--ice);
  }
  .letterhead__header .brand-dot { left: 466px; top: 20px; width: 66px; height: 66px; }
  .letterhead__header .wordmark {
    position: absolute; left: 0; right: 0; top: 96px;
    font-size: 21px; line-height: 24px;
  }
  .letterhead__header .wordmark__sub { font-size: 10px; line-height: 13px; }

  .letterhead__footer {
    position: absolute; left: 0; top: 656px;
    width: 100%; height: 124px;
    background: var(--sky);
  }
  .office { position: absolute; left: 52px; top: 18px; }
  .office__pin { position: absolute; left: 0; top: 4px; width: 20px; height: 24px; fill: var(--ink); }
  .office__name {
    margin: 0 0 0 30px;
    font-family: "Ubuntu", sans-serif; font-weight: 700;
    font-size: 22px; line-height: 28px; color: var(--ink);
  }
  .office__name span { color: var(--white); }
  .office__address {
    margin: 4px 0 0 28px; font-style: normal;
    font-family: "Source Sans 3", sans-serif;
    font-size: 17px; line-height: 25px; color: var(--ink);
  }
  .footer-divider {
    position: absolute; left: 500px; top: 18px;
    width: 1px; height: 86px; background: var(--ink);
  }
  .letterhead__footer .contact-list { left: 547px; top: 18px; font-size: 17px; }
  .letterhead__footer .contact-list li { height: 25.5px; }
  .letterhead__footer .contact-list svg { width: 18px; height: 18px; margin-right: 10px; }
</style>
</head>
<body>
<main class="stage">

  <section class="card card--back" aria-label="Business card back">
    <div class="pattern-field" role="img" aria-label="Repeating brand symbol pattern"></div>
    <p class="wordmark">HARLOW REACH<span class="wordmark__sub">CONSULTING</span></p>
  </section>

  <section class="card card--front" aria-label="Business card front">
    <div class="card__top">
      <span class="brand-dot" aria-hidden="true"></span>
      <p class="wordmark">HARLOW REACH<span class="wordmark__sub">CONSULTING</span></p>
    </div>
    <div class="card__band">
      <div class="person">
        <p class="person__name">Dara <strong>Ellison</strong></p>
        <p class="person__role">director of marketing</p>
      </div>
      <ul class="contact-list">
        <li>
          <svg viewBox="0 0 24 24" aria-hidden="true"><path d="M6.6 10.8a15.1 15.1 0 0 0 6.6 6.6l2.2-2.2a1 1 0 0 1 1-.25 11.4 11.4 0 0 0 3.6.57 1 1 0 0 1 1 1V20a1 1 0 0 1-1 1A17 17 0 0 1 3 4a1 1 0 0 1 1-1h3.5a1 1 0 0 1 1 1c0 1.25.2 2.45.57 3.57a1 1 0 0 1-.25 1z"/></svg>
          +1 404 555018
        </li>
        <li>
          <svg viewBox="0 0 24 24" aria-hidden="true"><path d="M2 5h20v14H2z M3.5 6.5 12 13l8.5-6.5" fill="none" stroke="#0B1C2C" stroke-width="0"/><path d="M2 5h20v14H2zm2 2v.3l8 5.6 8-5.6V7zm0 2.7V17h16V9.7l-8 5.6z"/></svg>
          dara.ellison@harlowreach.com
        </li>
        <li>
          <svg viewBox="0 0 24 24" aria-hidden="true"><path d="M12 2a10 10 0 1 0 0 20 10 10 0 0 0 0-20zm-1 2.1V11H7.05c.15-3.1 1.7-5.9 3.95-6.9zm2 0c2.25 1 3.8 3.8 3.95 6.9H13zM4.07 11h1c.1-2 .6-3.8 1.5-5.2A8 8 0 0 0 4.07 11zm14.9 0h1A8 8 0 0 0 17.4 5.8c.9 1.4 1.4 3.2 1.55 5.2zM4.07 13a8 8 0 0 0 2.5 5.2c-.9-1.4-1.4-3.2-1.5-5.2zm2.98 0H11v6.9c-2.25-1-3.8-3.8-3.95-6.9zM13 13h3.95c-.15 3.1-1.7 5.9-3.95 6.9zm5.95 0c-.15 2-.65 3.8-1.55 5.2A8 8 0 0 0 19.93 13z"/></svg>
          www.harlowreach.com
        </li>
      </ul>
    </div>
  </section>

  <section class="letterhead" aria-label="Document letterhead">
    <header class="letterhead__header">
      <span class="brand-dot" aria-hidden="true"></span>
      <p class="wordmark">HARLOW REACH<span class="wordmark__sub">CONSULTING</span></p>
    </header>
    <footer class="letterhead__footer">
      <div class="office">
        <svg class="office__pin" viewBox="0 0 20 24" aria-hidden="true"><path d="M10 0a9 9 0 0 0-9 9c0 6.5 9 15 9 15s9-8.5 9-15a9 9 0 0 0-9-9zm0 5.5a3.5 3.5 0 1 1 0 7 3.5 3.5 0 0 1 0-7zm0 1.8a1.7 1.7 0 1 0 0 3.4 1.7 1.7 0 0 0 0-3.4z" fill-rule="evenodd"/></svg>
        <p class="office__name"><span>Harlow Reach</span> consulting</p>
        <address class="office__address">250 Liberty Road, 300 East<br>Marlow, Columbia, 32107</address>
      </div>
      <span class="footer-divider" aria-hidden="true"></span>
      <ul class="contact-list">
        <li>
          <svg viewBox="0 0 24 24" aria-hidden="true"><path d="M6.6 10.8a15.1 15.1 0 0 0 6.6 6.6l2.2-2.2a1 1 0 0 1 1-.25 11.4 11.4 0 0 0 3.6.57 1 1 0 0 1 1 1V20a1 1 0 0 1-1 1A17 17 0 0 1 3 4a1 1 0 0 1 1-1h3.5a1 1 0 0 1 1 1c0 1.25.2 2.45.57 3.57a1 1 0 0 1-.25 1z"/></svg>
          +1 404 555018
        </li>
        <li>
          <svg viewBox="0 0 24 24" aria-hidden="true"><path d="M2 5h20v14H2zm2 2v.3l8 5.6 8-5.6V7zm0 2.7V17h16V9.7l-8 5.6z"/></svg>
          information@harlowreach.com
        </li>
        <li>
          <svg viewBox="0 0 24 24" aria-hidden="true"><path d="M12 2a10 10 0 1 0 0 20 10 10 0 0 0 0-20zm-1 2.1V11H7.05c.15-3.1 1.7-5.9 3.95-6.9zm2 0c2.25 1 3.8 3.8 3.95 6.9H13zM4.07 11h1c.1-2 .6-3.8 1.5-5.2A8 8 0 0 0 4.070 11zm14.9 0h1A8 8 0 0 0 17.4 5.8c.9 1.4 1.4 3.2 1.55 5.2zM4.07 13a8 8 0 0 0 2.5 5.2c-.9-1.4-1.4-3.2-1.5-5.2zm2.98 0H11v6.9c-2.25-1-3.8-3.8-3.95-6.9zM13 13h3.95c-.15 3.1-1.7 5.9-3.95 6.9zm5.95 0c-.15 2-.65 3.8-1.55 5.2A8 8 0 0 0 19.93 13z"/></svg>
          www.harlowreach.com
        </li>
      </ul>
    </footer>
  </section>

</main>
</body>
</html>
```